Home page web design for a lawn specialist business

-The design must be based around the attached HPID (home page information design) called Turf Haven HPID. I've attached Word and PDF versions - these are the same. The table boxes are just for approximate placement of information and you can use boxes and bold shapes for this design.

All fonts used in the HPID are only examples - you can use any Google font you wish.

- Text that is in orange is for your information only. Text to go on the design is black. Some instructions are in the HPID. Please be creative!

-The design needs to be modern and exciting - colours are to be the green of the logo, and white ...and then choose dark green, or dark grey or black.

Logo - attached (it's not great quality but don't worry, we'll replace it later)

- I've provided the images for the galleries - they are labelled and will match the name in the HPID. Please use the supplied images!

- Examples of some websites that have great design... don't copy them please but they are similar in look to what we are after....
www.kelbrinworks.co.nz
http://www.rimsafe-guarding.co.nz/
http://www.brightnest.wb.gs/

Important: Width of content will be 1280 pixels when implemented as a web page but the winning design will need to supplied be on a 2000 pixel wide background so nav bars and background can extend outside the 1280 width.
Header height (without nav bar) 150-160 pixels.

We don't comment on individual designs but will choose a winning design promptly.

Industry/Entity Type

Business

Number of Pages Required

1 page

Font styles to use
Sans Serif

Requirements
Must have
• clean, modern, well-spaced design

```html
<!DOCTYPE html>
<html lang="en">
<head>
<meta charset="utf-8">
<title>Turf Haven – Lawn Specialists</title>
<link rel="stylesheet" href="https://fonts.googleapis.com/css2?family=Noto+Serif:wght@400;700&family=Arimo:wght@400;700&display=swap">
<style>
:root{
  --green:#4c9b2b;
  --green-light:#6cb841;
  --green-dark:#1f3d14;
  --green-deep:#16300e;
  --white:#ffffff;
  --ink:#333333;
  --muted:#555555;
  --line:#8cc46a;
}
*{box-sizing:border-box;margin:0;padding:0}
html,body{width:808px;height:1200px;overflow:hidden;background:var(--white)}
body{position:relative;font-family:"Arimo",Arial,sans-serif;color:var(--ink)}
.abs{position:absolute}

/* header */
.brand{left:86px;top:14px;height:48px;display:flex;align-items:center;gap:7px;white-space:nowrap}
.brand-mark{width:14px;height:14px;background:var(--green)}
.brand-name{font-family:"Noto Serif",Georgia,serif;font-weight:700;font-size:20px;line-height:22px;color:var(--green)}
.header-info{right:83px;top:7px;text-align:right;white-space:nowrap}
.header-title{font-family:"Noto Serif",Georgia,serif;font-size:16px;line-height:19px;color:#333}
.header-tag{font-size:7.8px;line-height:10px;color:#333;margin-top:5px;display:flex;gap:5px;justify-content:flex-end;align-items:flex-start}
.header-phone{font-size:11px;line-height:14px;color:#222;margin-top:5px;display:flex;gap:6px;justify-content:flex-end;align-items:center}

/* nav */
.nav{left:0;top:73px;width:808px;height:24px;background:var(--green)}
.nav ul{list-style:none;display:flex;position:absolute;left:85px;top:0;height:24px}
.nav li{font-family:"Noto Serif",Georgia,serif;font-size:8.6px;color:var(--white);padding:0 11.5px;line-height:24px;border-right:1px solid rgba(0,0,0,.12);white-space:nowrap}
.nav li:last-child{border-right:0}
.nav li.active{color:#1b3510}

/* hero */
.hero{left:0;top:97px;width:808px;height:202px}
.hero svg{display:block}
.hero-toggle{left:324px;top:241px;width:136px;height:23px;background:var(--green-light);display:flex;align-items:center;justify-content:space-around;color:var(--white);font-family:"Noto Serif",Georgia,serif;font-size:11px}
.hero-toggle span{display:flex;align-items:center;gap:4px}

/* intro */
.intro{left:0;top:312px;width:808px;text-align:center}
.intro-title{font-family:"Noto Serif",Georgia,serif;font-size:10px;line-height:12.5px;color:#444}
.intro-rule{margin:8px auto 9px;width:190px;height:4px;border-top:1px solid var(--line);border-bottom:1px solid var(--line)}
.intro p{font-size:6.6px;line-height:9px;color:var(--muted);width:520px;margin:0 auto 6px}

/* cards */
.card{top:418px;width:154px;height:176px;border:1px solid var(--line);background:var(--white)}
.card-head{height:21px;background:var(--green);color:var(--white);font-family:"Noto Serif",Georgia,serif;font-weight:700;font-size:7px;line-height:21px;padding-left:8px;white-space:nowrap}
.card-img{margin:3px 3px 0;height:76px}
.card-text{font-size:6.6px;line-height:10.4px;color:var(--muted);padding:6px 5px 0 5px;border-top:1px solid var(--line);margin-top:3px;height:51px}
.btn-outline{display:inline-block;border:1px solid var(--green);border-radius:3px;font-size:6.8px;color:var(--muted);padding:3px 6px;margin-left:3px}

/* video */
.feature{left:0;top:624px;width:808px;height:278px;background:radial-gradient(ellipse at 30% 40%,#2d5a1c 0%,var(--green-dark) 60%,var(--green-deep) 100%)}
.feature-title{left:83px;top:642px;width:316px;font-family:"Noto Serif",Georgia,serif;font-weight:400;font-size:12.6px;line-height:15.5px;color:var(--white);padding-bottom:5px;border-bottom:1px dashed rgba(255,255,255,.55)}
.screen{left:113px;top:695px;width:254px;height:173px;border:7px solid #151515;border-radius:7px 7px 0 0;background:linear-gradient(180deg,#9aab92 0%,#6f8f5a 38%,#5ea73a 62%,#3f7a2a 100%)}
.laptop-base{left:84px;top:866px;width:311px;height:6px;background:#2a2a2a;border-radius:0 0 4px 4px}
.play{left:221px;top:774px;width:24px;height:24px;border:2px solid rgba(255,255,255,.75);border-radius:50%}
.about-title{left:466px;top:660px;width:260px;font-family:"Noto Serif",Georgia,serif;font-weight:400;font-size:13px;color:var(--white);padding-bottom:4px;border-bottom:1px dashed rgba(255,255,255,.55)}
.about-list{left:466px;top:693px;width:260px;list-style:none}
.about-list li{display:flex;gap:9px;font-size:7.6px;line-height:12px;color:var(--white);margin-bottom:8px}
.about-list svg{flex:none;margin-top:3px}
.btn-light{left:466px;top:826px;border:1px solid var(--white);border-radius:3px;color:var(--white);font-size:7px;padding:3px 5px}

/* reviews */
.reviews{left:0;top:902px;width:808px;height:140px;background:linear-gradient(90deg,#35432d 0%,#4d6a3a 45%,#577a3c 100%)}
.reviews-title{left:0;top:920px;width:808px;text-align:center;font-family:"Noto Serif",Georgia,serif;font-weight:400;font-size:13px;color:var(--white)}
.reviews-rule{left:328px;top:941px;width:152px;border-top:1px dashed rgba(255,255,255,.6)}
.quote{left:0;top:960px;width:808px;text-align:center;font-size:10px;color:var(--white)}
.quote-mark{font-family:"Noto Serif",Georgia,serif;font-size:22px;color:rgba(255,255,255,.6);vertical-align:-6px;margin:0 5px}
.reviewer{left:0;top:991px;width:808px;text-align:center;font-size:10px;line-height:12.5px;color:var(--white)}

/* footer */
.footer{left:0;top:1042px;width:808px;height:134px;background:var(--green-light)}
.foot-head{font-size:7px;font-weight:700;color:var(--white);padding-bottom:4px;border-bottom:1px solid rgba(255,255,255,.5)}
.quick-links{left:87px;top:1052px;width:80px}
.quick-links ul{list-style:none;margin-top:6px}
.quick-links li{font-size:6.8px;line-height:11.3px;color:var(--white);padding-left:9px;position:relative}
.quick-links li::before{content:"";position:absolute;left:1px;top:3px;border-left:3px solid var(--white);border-top:2px solid transparent;border-bottom:2px solid transparent}
.foot-divider{top:1075px;height:90px;border-left:1px solid rgba(0,0,0,.15)}
.diploma{left:221px;top:1052px;width:108px}
.badge{left:221px;top:1071px;width:97px;height:100px;background:var(--white)}
.badge-shape{position:absolute;left:18px;top:12px;width:61px;height:61px;border-radius:50%;background:#9ccf5a}
.inquiry{left:383px;top:1052px;width:74px}
.inquiry-note{left:385px;top:1070px;font-family:"Noto Serif",Georgia,serif;font-size:7px;line-height:9px;color:var(--white)}
.field{background:var(--white);font-size:6.8px;font-style:italic;color:#666;padding:6px 7px;height:19px}
.btn-dark{left:650px;top:1152px;width:66px;height:16px;border:1.5px solid #111;border-radius:3px;font-size:7px;color:#111;text-align:center;line-height:13px}
.copyright{left:0;top:1176px;width:808px;height:24px;background:linear-gradient(180deg,#5c9a2c,#3f7a1e);color:var(--white);font-size:6px;text-align:center;line-height:24px}
</style>
</head>
<body>

<header>
  <div class="abs brand"><span class="brand-mark"></span><span class="brand-name">Turf Haven</span></div>
  <div class="abs header-info">
    <div class="header-title">Lawn specialists</div>
    <div class="header-tag">
      <svg width="9" height="13" viewBox="0 0 9 13"><path d="M4.5 0C2 0 0 2 0 4.5 0 8 4.5 13 4.5 13S9 8 9 4.5C9 2 7 0 4.5 0Z" fill="#4c9b2b"/><circle cx="4.5" cy="4.5" r="1.8" fill="#fff"/></svg>
      <div>...from ground preparation to lawn aftercare<br>Servicing the Auckland region</div>
    </div>
    <div class="header-phone">
      <svg width="14" height="14" viewBox="0 0 15 15"><circle cx="7.5" cy="7.5" r="6.8" fill="none" stroke="#4c9b2b" stroke-width="1.2"/><path d="M5 4c-1 1-.6 3 .8 4.6S9 11 10.2 10l.6-.8-1.6-1.2-.8.7c-.7-.2-1.7-1.2-1.9-1.9l.7-.8L6 4.4Z" fill="#4c9b2b"/></svg>
      0800 42 61 90
    </div>
  </div>
</header>

<nav class="abs nav">
  <ul>
    <li class="active">Home</li><li>About Us</li><li>Services</li><li>Lawn Care</li><li>Seasonal Care</li><li>Hydroseeding</li><li>FAQ's</li><li>Before &amp; After Gallery</li><li>Quote / Contact</li>
  </ul>
</nav>

<section class="abs hero" role="img" aria-label="Before and after photo of a front yard: bare hydroseeded ground on the left, a lush green lawn on the right">
  <svg width="808" height="202" viewBox="0 0 808 202">
    <defs>
      <linearGradient id="before" x1="0" y1="0" x2="0" y2="1">
        <stop offset="0" stop-color="#8e9a88"/><stop offset=".45" stop-color="#7b8576"/><stop offset=".6" stop-color="#4f7670"/><stop offset="1" stop-color="#3f6762"/>
      </linearGradient>
      <linearGradient id="after" x1="0" y1="0" x2="0" y2="1">
        <stop offset="0" stop-color="#9fb0a8"/><stop offset=".38" stop-color="#8f948a"/><stop offset=".55" stop-color="#6fb83a"/><stop offset="1" stop-color="#4a9424"/>
      </linearGradient>
    </defs>
    <rect width="808" height="202" fill="url(#before)"/>
    <polygon points="436,0 808,0 808,202 380,202" fill="url(#after)"/>
    <line x1="436" y1="0" x2="380" y2="202" stroke="#1a1a1a" stroke-width="3"/>
  </svg>
</section>
<div class="abs hero-toggle">
  <span><svg width="11" height="8" viewBox="0 0 11 8"><path d="M0 4 4 0v2.5h7v3H4V8Z" fill="#d9efc6"/></svg>Before</span>
  <span>After<svg width="11" height="8" viewBox="0 0 11 8"><path d="M11 4 7 0v2.5H0v3h7V8Z" fill="#d9efc6"/></svg></span>
</div>

<section class="abs intro">
  <div class="intro-title">You can always spot a Turf Haven lawn<br>It's the one that turns your neighbours green with envy</div>
  <div class="intro-rule"></div>
  <p>If you want a lawn or playing field that looks good throughout the year, talk to us. Turf Haven are New Zealand's experts in high quality grass seeding and lawn maintenance, creating the lushest lawns you'll ever see. With high-tech equipment, years of experience and expert aftercare, nobody knows grass like Turf Haven</p>
  <p>There are many factors that influence the quality of a lawn, including seasonality, growing conditions, shade, seed types, and time. A one-size-fits-all solution couldn't possibly guarantee a great lawn, so we provide personalised advice, a full range of seeding techniques</p>
</section>

<article class="abs card" style="left:82px">
  <div class="card-head">Grass Seeding Services</div>
  <div class="card-img" role="img" aria-label="Freshly hydroseeded garden bed" style="background:linear-gradient(180deg,#5c6a52 0%,#6f8d5a 30%,#4f8078 55%,#4a7a74 100%)"></div>
  <div class="card-text">With a wide range of grass seed applications to choose from, including hydroseeding and instant lawn, there is an option to suit your property and your requirements.</div>
  <span class="btn-outline">Find out more</span>
</article>
<article class="abs card" style="left:245px">
  <div class="card-head">Lawn Care Maintenance</div>
  <div class="card-img" role="img" aria-label="Sprinkler watering a lawn" style="background:radial-gradient(ellipse at 50% 75%,#c7d8b6 0%,#7fb04a 35%,#3f7d22 100%)"></div>
  <div class="card-text">As well as lawn care services, the team at Turf Haven provides helpful information for regular upkeep of your residential or commercial lawn.</div>
  <span class="btn-outline">Find out more</span>
</article>
<article class="abs card" style="left:408px">
  <div class="card-head">FAQs About Grass Seeding &amp; Lawn Care</div>
  <div class="card-img" role="img" aria-label="Established green lawn beside a fence" style="background:linear-gradient(180deg,#d4d6ce 0%,#b9b8ab 38%,#6faa3e 48%,#3f9a2a 100%)"></div>
  <div class="card-text">For more information, read our frequently asked questions regarding grass seeding and lawn care.</div>
  <span class="btn-outline">Find out more</span>
</article>
<article class="abs card" style="left:571px">
  <div class="card-head">Before And After Lawn Photos</div>
  <div class="card-img" role="img" aria-label="Before and after lawn seeding photo" style="background:linear-gradient(90deg,#5d7a72 0%,#5d7a72 54%,#222 54%,#222 55%,#5da534 55%,#5da534 100%)"></div>
  <div class="card-text">See what you potential new lawn could look like by viewing a range of before and after lawn seeding photos.</div>
  <span class="btn-outline">Find out more</span>
</article>

<section class="abs feature" role="img" aria-label="Dark green grass background"></section>
<h2 class="abs feature-title">Watch the video on how Turf Haven can transform your empty spaces into beautiful green grass lawns</h2>
<div class="abs screen" role="img" aria-label="Video still of a finished garden lawn"></div>
<div class="abs laptop-base"></div>
<div class="abs play"><svg width="20" height="20" viewBox="0 0 20 20"><path d="M7 5v10l8-5Z" fill="rgba(255,255,255,.8)"/></svg></div>

<h2 class="abs about-title">Turf Haven</h2>
<ul class="abs about-list">
  <li><svg width="10" height="10" viewBox="0 0 10 10"><circle cx="5" cy="5" r="5" fill="#fff"/><path d="M2.6 5 4.3 6.7 7.6 3.3" stroke="#1f3d14" stroke-width="1.4" fill="none"/></svg><span>For all things grass, you need the best! Turf Haven are skilled specialists when it comes to creating the perfect lawn for your property.</span></li>
  <li><svg width="10" height="10" viewBox="0 0 10 10"><circle cx="5" cy="5" r="5" fill="#fff"/><path d="M2.6 5 4.3 6.7 7.6 3.3" stroke="#1f3d14" stroke-width="1.4" fill="none"/></svg><span>From pre-seeding preparation to a full range of grass seeding services and lawn after care options, you'll enjoy a healthy green lawn for many years.</span></li>
  <li><svg width="10" height="10" viewBox="0 0 10 10"><circle cx="5" cy="5" r="5" fill="#fff"/><path d="M2.6 5 4.3 6.7 7.6 3.3" stroke="#1f3d14" stroke-width="1.4" fill="none"/></svg><span>Selling your property?<br>Turf Haven will add the wow factor to the outdoor areas of your home with a lush green lawn.</span></li>
</ul>
<span class="abs btn-light">Find out more</span>

<section class="abs reviews" role="img" aria-label="Lawn mower on a freshly cut lawn"></section>
<h2 class="abs reviews-title">Happy Customer Reviews</h2>
<div class="abs reviews-rule"></div>
<p class="abs quote"><span class="quote-mark">&ldquo;</span>I would recommend Turf Haven to anyone who wants an amazing lawn.<span class="quote-mark">&rdquo;</span></p>
<p class="abs reviewer">Dana Reid<br>Homeowner, Takapuna</p>

<footer class="abs footer"></footer>
<div class="abs quick-links">
  <div class="foot-head">QUICK LINKS</div>
  <ul>
    <li>Home</li><li>About Us</li><li>Services</li><li>Lawn Care</li><li>Seasonal Care</li><li>Hydroseeding</li><li>FAQ's</li><li>Before &amp; After Gallery</li><li>Quote / Contact</li>
  </ul>
</div>
<div class="abs foot-divider" style="left:193px"></div>
<div class="abs diploma"><div class="foot-head">DIPLOMA IN HORTICULTURE</div></div>
<div class="abs badge" role="img" aria-label="Horticulture diploma badge"><span class="badge-shape"></span></div>
<div class="abs foot-divider" style="left:356px"></div>
<div class="abs inquiry"><div class="foot-head">QUICK INQUIRY</div></div>
<p class="abs inquiry-note">Get a quote for your new lawn!<br>Fill in the form or phone us on 0800 42 61 90.</p>
<div class="abs field" style="left:385px;top:1094px;width:124px">First Name</div>
<div class="abs field" style="left:514px;top:1094px;width:125px">Last Name</div>
<div class="abs field" style="left:385px;top:1118px;width:124px">Email Address</div>
<div class="abs field" style="left:514px;top:1118px;width:125px">Contact Number</div>
<div class="abs field" style="left:385px;top:1141px;width:254px;height:30px">Message</div>
<div class="abs btn-dark">CALL ME BACK</div>
<div class="abs copyright">Copyright ©2015. Turf Haven. All Rights Reserved</div>

</body>
</html>
```